Business Card Design

We are a General Practice - Family medicine
We also have Allied Health professionals working within our team

Industry/Entity Type

Business

Contact Information for Business Card

Front of the card to display:

BRAMBLEWICK MEDICAL
PHONE 6348 2917

5/41 Fennimore Parade
Launceston Tasmania 7284

Back of the card to display:

My Appointments
Date:
Time:
With:

Please remember to phone us on 6348 2917 to cancel your appointment if you can't keep it.
A fee applied to missed appointments

```html
<!DOCTYPE html>
<html lang="en">
<head>
<meta charset="utf-8">
<title>Bramblewick Medical – Business Card</title>
<link href="https://fonts.googleapis.com/css2?family=Arimo:wght@400;700&display=swap" rel="stylesheet">
<style>
  :root {
    --backdrop: #9cff00;
    --card: #ffffff;
    --cyan: #3fd3f7;
    --cyan-soft: #9fe8fb;
    --green: #9be62e;
    --green-soft: #d8f5a8;
    --grey: #8a8a8a;
  }
  * { margin: 0; padding: 0; box-sizing: border-box; }
  html, body {
    width: 1200px; height: 742px; overflow: hidden;
    background: var(--backdrop);
    font-family: "Arimo", Arial, sans-serif;
  }
  .canvas { position: relative; width: 1200px; height: 742px; }
  .card {
    position: absolute; top: 219px;
    width: 519px; height: 303px;
    background: var(--card); overflow: hidden;
  }
  .card--front { left: 41px; }
  .card--back { left: 640px; }

  .petal-motif {
    position: absolute; left: 0; top: 0;
    width: 178px; height: 178px;
    background:
      radial-gradient(circle at 62% 30%, var(--green) 0%, var(--green-soft) 45%, transparent 70%),
      radial-gradient(circle at 28% 72%, var(--cyan) 0%, var(--cyan-soft) 45%, transparent 70%);
    border-bottom-right-radius: 60%;
  }

  .front-contact {
    position: absolute; top: 18px; left: 392px; width: 112px;
    text-align: center; font-weight: 700; font-size: 12.5px; line-height: 1.15;
  }
  .front-contact .name-first { color: var(--cyan); }
  .front-contact .name-second { color: var(--green); }
  .front-contact .phone { color: var(--cyan); }
  .front-contact .phone span { color: var(--green); }

  .brand {
    position: absolute; top: 200px; left: 150px;
    display: flex; align-items: center; gap: 8px;
  }
  .brand-dot {
    width: 26px; height: 26px; border-radius: 50%;
    background: var(--green);
  }
  .brand-name {
    color: var(--cyan); font-size: 23px; font-weight: 400;
    white-space: nowrap;
  }

  .address {
    position: absolute; left: 0; right: 0; top: 245px;
    text-align: center; color: var(--cyan-soft);
    font-weight: 700; font-size: 13.5px; letter-spacing: 1.6px;
  }

  .appointments-title {
    position: absolute; top: 27px; left: 300px; width: 200px;
    text-align: center; color: var(--green-soft);
    font-weight: 700; font-size: 14px;
  }
  .appointment-field {
    position: absolute; left: 325px;
    color: var(--grey); font-size: 14.5px;
  }
  .field-date { top: 67px; }
  .field-time { top: 120px; }
  .field-with { top: 174px; }

  .cancel-note {
    position: absolute; left: 0; right: 0; top: 282px;
    text-align: center; color: var(--cyan); font-size: 11px;
    white-space: nowrap;
  }
</style>
</head>
<body>
<main class="canvas">
  <section class="card card--front" aria-label="Card front">
    <div class="petal-motif" role="img" aria-label="Large green and blue petal decoration in the corner"></div>
    <div class="front-contact">
      <div><span class="name-first">Bramblewick</span><span class="name-second">Medical</span></div>
      <div class="phone">6348 <span>2917</span></div>
    </div>
    <div class="brand">
      <span class="brand-dot"></span>
      <span class="brand-name">Bramblewick Medical</span>
    </div>
    <p class="address">5/41 Fennimore Parade Launceston Tasmania 7284</p>
  </section>

  <section class="card card--back" aria-label="Card back">
    <div class="petal-motif" role="img" aria-label="Large green and blue petal decoration in the corner"></div>
    <h2 class="appointments-title">My Appointments</h2>
    <p class="appointment-field field-date">Date -</p>
    <p class="appointment-field field-time">Time -</p>
    <p class="appointment-field field-with">With -</p>
    <p class="cancel-note">Please remember to phone us on 6348 2917 to cancel your appointment if you can't keep it</p>
  </section>
</main>
</body>
</html>
```